Business Card Design

I'm a commercial general contractor remodel offices, hotels, health clubs and stores mostly San Francisco and the peninsula
the file I down loaded is kind of what I want I like the I beam with my company name in it, that would be fine with me but if you have better Idea will look at it you never know, I'm decided to give in and change my company name to how every one knows me, I have been in business since 1991, I like the I beam logo I included one of my old card from my old company for reference for you.

Industry/Entity Type

Business

Contact Information for Business Card

BRAXO CONSTRUCTION (is my company name)
Wendell Trusk contractor, LIc 314827
4158 Garnet Row, San Bruno, California 94066
mobile, (415) 555-0147
phone (650) 555-0182
Fax, (650) 555-0183
email, braxo@braxoconstruction.example

```html
<!DOCTYPE html>
<html lang="en">
<head>
<meta charset="utf-8">
<title>Braxo Design &amp; Construction – Business Card</title>
<link rel="stylesheet" href="https://fonts.googleapis.com/css2?family=Open+Sans:wght@400;700&display=swap">
<style>
  :root {
    --page-bg: #e9e7e4;
    --front-top: #0a86ad;
    --front-bottom: #05254f;
    --front-mark: #2f7fc2;
    --brand-blue: #1f6fbf;
    --accent-blue: #2a7fd0;
    --swoosh-line: #111111;
    --ink: #333333;
    --ink-dark: #1a1a1a;
    --name-blue: #1d3f73;
    --card-white: #ffffff;
  }
  * { margin: 0; padding: 0; box-sizing: border-box; }
  html, body { width: 1200px; height: 900px; overflow: hidden; }
  body {
    background: var(--page-bg);
    font-family: "Open Sans", Arial, sans-serif;
    position: relative;
  }
  .card {
    position: absolute;
    top: 290px;
    width: 560px;
    height: 320px;
    border-radius: 4px;
    box-shadow: 0 6px 18px rgba(0,0,0,0.18);
    overflow: hidden;
  }
  .card--front {
    left: 30px;
    background: linear-gradient(180deg, var(--front-top) 0%, var(--front-bottom) 100%);
  }
  .card--back {
    left: 610px;
    background: var(--card-white);
  }

  /* Front */
  .front-brand {
    position: absolute;
    inset: 0;
    display: flex;
    flex-direction: column;
    align-items: center;
    justify-content: center;
    color: var(--front-mark);
    font-weight: 700;
  }
  .front-brand__name { font-size: 86px; letter-spacing: 4px; line-height: 1; }
  .front-brand__tag { font-size: 21px; letter-spacing: 2px; margin-top: 8px; }

  /* Back */
  .corner-swoosh { position: absolute; top: 0; right: 0; width: 260px; height: 90px; }
  .corner-swoosh__fill { fill: var(--accent-blue); }
  .corner-swoosh__line { fill: none; stroke: var(--swoosh-line); stroke-width: 5; }

  .firm-badge {
    position: absolute;
    top: 72px;
    right: 70px;
    display: flex;
    align-items: flex-end;
    gap: 8px;
  }
  .firm-badge__name { font-size: 22px; font-weight: 700; color: var(--brand-blue); line-height: 1; }
  .firm-badge__lic { font-size: 10px; color: var(--ink); line-height: 1; }

  .back-brand {
    position: absolute;
    top: 128px;
    right: 28px;
    text-align: right;
    font-weight: 700;
  }
  .back-brand__name { font-size: 54px; color: var(--brand-blue); letter-spacing: 3px; line-height: 1; }
  .back-brand__tag { font-size: 13px; color: var(--ink-dark); letter-spacing: 1px; margin-top: 4px; }

  .person { position: absolute; top: 112px; left: 34px; }
  .person__name { font-size: 17px; font-weight: 700; color: var(--name-blue); line-height: 1.3; }
  .person__role { font-size: 12px; color: var(--ink); }

  .contact {
    position: absolute;
    top: 178px;
    left: 34px;
    font-size: 12.5px;
    line-height: 1.32;
    color: var(--ink);
    list-style: none;
  }
  .contact__label { color: var(--accent-blue); }
  .contact__web { color: var(--ink-dark); }
  .contact__web span { color: var(--accent-blue); }
</style>
</head>
<body>

  <section class="card card--front" aria-label="Card front">
    <div class="front-brand">
      <span class="front-brand__name">BRAXO</span>
      <span class="front-brand__tag">DESIGN &amp; CONSTRUCTION</span>
    </div>
  </section>

  <section class="card card--back" aria-label="Card back">
    <svg class="corner-swoosh" viewBox="0 0 260 90" aria-hidden="true">
      <path class="corner-swoosh__fill" d="M40 0 H260 V70 C220 30 140 8 40 0 Z"/>
      <path class="corner-swoosh__line" d="M40 0 C140 8 220 30 260 70"/>
    </svg>

    <div class="firm-badge">
      <span class="firm-badge__name">BD&amp;C, INC</span>
      <span class="firm-badge__lic">Lic#314827</span>
    </div>

    <div class="back-brand">
      <div class="back-brand__name">BRAXO</div>
      <div class="back-brand__tag">DESIGN &amp; CONSTRUCTION</div>
    </div>

    <div class="person">
      <div class="person__name">Wendell Trusk</div>
      <div class="person__role">President</div>
    </div>

    <ul class="contact">
      <li>4158 Garnet Row</li>
      <li>Larkfield, Ca 94088</li>
      <li><span class="contact__label">T:</span> 650 555 - 0182</li>
      <li><span class="contact__label">C:</span> 415 555 - 0147</li>
      <li><span class="contact__label">F:</span> 650 555 - 0183</li>
      <li><span class="contact__label">E:</span> braxo@braxomail.example</li>
      <li class="contact__web">www.<span>braxodesignconstruction</span>.example</li>
    </ul>
  </section>

</body>
</html>
```